tilebaron.org needs a cool website!

I need a website designed for a commercial flooring maintenance company based in Texas. We will be providing services like carpet shampooing, burnishing, resurfacing and power washing. It needs to be cool and trendy.

I’ll need 10-20 pages. I need help deciding on the style and color palette. We will need great stock pictures of different flooring types and you will need to photo shop our logo on imaginary cars or storefronts.

Please have similar experience and an open mind. I’m looking for a partnership and someone to turn to for future projects and upkeep.

The domain is currently hosted on Wix. You will need the ability to develop and code it there.
Updates

Target Market(s)

Commercial businesses and properties

Industry/Entity Type

Floor care

Coding

Coded - Design and coding required

Number of Pages Required

5+ page

Requirements
Must have
• Great pictures of different types of floors.

```html
<!DOCTYPE html>
<html lang="en">
<head>
<meta charset="utf-8">
<title>Tilebaron — Commercial Floor Care</title>
<link rel="stylesheet" href="https://fonts.googleapis.com/css2?family=Heebo:wght@400;500;700;800&family=Roboto:wght@500;700;900&display=swap">
<style>
:root{
  --green:#6cb52d;
  --green-dark:#213a13;
  --ink:#111;
  --text:#444;
  --muted:#777;
  --soft:#eef2f6;
  --white:#fff;
  --line:#dfe3e8;
}
*{box-sizing:border-box;margin:0;padding:0}
html,body{width:1200px;height:4890px;overflow:hidden}
body{font-family:"Heebo",sans-serif;color:var(--text);background:var(--white);position:relative}
.abs{position:absolute}
.tick{width:34px;height:5px;border-radius:3px;background:var(--green);display:block}
.center{left:0;right:0;text-align:center}
.center .tick{margin:0 auto}
.label{font:500 16px "Heebo",sans-serif;color:var(--green);text-transform:uppercase;letter-spacing:.5px}
.title{font:900 42px "Roboto",sans-serif;color:var(--ink);text-transform:uppercase;letter-spacing:.3px}
.btn{display:inline-flex;align-items:center;justify-content:center;background:var(--green);color:#fff;font:700 14px "Heebo",sans-serif;text-transform:uppercase;border-radius:3px}

/* header + hero */
.hero{top:0;left:0;width:1200px;height:668px;background:linear-gradient(110deg,#0f1410 0%,#1d2620 45%,#2c3530 70%,#151a17 100%)}
.hero-figure{left:600px;top:40px;width:520px;height:560px;border-radius:40% 40% 30% 30%;background:radial-gradient(circle at 50% 40%,#5a6a68 0%,#2a3533 60%,rgba(20,26,24,0) 80%)}
.logo{font:500 34px "Heebo",sans-serif;color:#fff;display:flex;align-items:center;gap:10px}
.logo .dot{width:14px;height:14px;border-radius:50%;background:var(--green)}
.nav{top:24px;left:424px;display:flex;gap:54px;font:500 15px "Heebo",sans-serif;color:#fff}
.nav .on{color:var(--green)}
.quote{top:12px;left:976px;width:158px;height:48px}
.hero-title{font:900 44px/56px "Roboto",sans-serif;color:#fff;text-transform:uppercase}
.hero-title em{font-style:normal;color:var(--green)}
.hero-text{font:400 17px/26px "Heebo",sans-serif;color:#e6e6e6;width:390px}

/* partners */
.partners-title{font:500 16px "Heebo",sans-serif;color:var(--ink);letter-spacing:.6px}
.partners-title em{font-style:normal;color:var(--green)}
.partners{top:820px;left:66px;width:1068px;display:flex;justify-content:space-between;align-items:center}
.partner{display:flex;align-items:center;gap:8px;font:700 21px "Heebo",sans-serif;color:#666}
.partner i{width:16px;height:16px;background:#888;display:block}

/* welcome */
.welcome-frame{left:88px;top:940px;width:588px;height:405px;background:var(--green);border-radius:14px}
.welcome-photo{left:66px;top:962px;width:590px;height:404px;background:linear-gradient(160deg,#9aa0a2,#5f6567 60%,#3a3f41);border-radius:14px}
.play{left:334px;top:1136px;width:56px;height:56px;border-radius:50%;border:2px solid #fff}
.play:after{content:"";position:absolute;left:21px;top:16px;border-left:16px solid #fff;border-top:11px solid transparent;border-bottom:11px solid transparent}
.body-text{font:400 15px/26px "Heebo",sans-serif;color:var(--text)}

/* services */
.services-band{top:1458px;left:0;width:1200px;height:408px;background:var(--green-dark)}
.svc-img{top:1693px;width:344px;height:325px;border-radius:16px}
.svc-card{top:1957px;width:300px;height:213px;background:#fff;border-radius:8px;box-shadow:0 6px 22px rgba(0,0,0,.12);text-align:center;padding-top:20px}
.svc-card h3{font:700 21px "Roboto",sans-serif;color:var(--ink)}
.svc-card p{font:400 14px/22px "Heebo",sans-serif;color:var(--text);margin:12px 26px 0}
.svc-card .btn{width:154px;height:46px;margin-top:14px}

/* projects */
.sub-dark{font:400 15px/26px "Heebo",sans-serif;color:var(--ink)}
.tile{border-radius:2px}
.tile-text{color:#fff;text-align:center}
.tile-text b{display:block;font:700 16px "Heebo",sans-serif;letter-spacing:1px;margin-bottom:8px}
.tile-text span{font:400 12px "Heebo",sans-serif}

/* testimonials + contact */
.soft-bg{top:3015px;left:0;width:1200px;height:1005px;background:var(--soft)}
.quote-card{top:3222px;width:522px;height:208px;background:#fff;border-radius:10px}
.avatar{top:3222px;width:170px;height:240px;border-radius:50% 50% 50% 50%/40% 40% 60% 60%}
.quote-text{font:italic 400 14px/24px "Heebo",sans-serif;color:#555;width:310px}
.who b{display:block;font:700 14px "Heebo",sans-serif;color:var(--ink)}
.who span{font:400 12px "Heebo",sans-serif;color:var(--muted)}
.contact-photo{top:4020px;left:0;width:1200px;height:458px;background:linear-gradient(100deg,#2d3e49,#6b6f70 40%,#a46a3a 70%,#3a4650)}
.form-card{top:3660px;left:334px;width:532px;height:580px;background:#fff;border-radius:10px;box-shadow:0 4px 24px rgba(0,0,0,.08)}
.form-card .intro{text-align:center;font:400 16px/26px "Heebo",sans-serif;color:var(--ink);margin:24px 30px 0}
.field{position:absolute;left:32px;width:466px;height:46px;border:1px solid var(--line);border-radius:2px;font:400 12px "Heebo",sans-serif;color:#666;padding:0 14px;display:flex;align-items:center;justify-content:space-between}
.field.active{background:#eef6e6;border-color:#cfe3bb}
.field.msg{height:128px;align-items:flex-start;padding-top:14px}
.field svg{width:14px;height:14px;stroke:#666;fill:none;stroke-width:1.6}

/* footer */
.footer-logo{font:500 44px "Heebo",sans-serif;color:var(--ink);display:flex;align-items:center;gap:12px}
.footer-logo .dot{width:18px;height:18px;border-radius:50%;background:var(--green)}
.f-head{font:700 14px "Heebo",sans-serif;color:var(--green);text-transform:uppercase}
.f-head:after{content:"";display:block;width:36px;height:3px;background:var(--green);margin-top:5px}
.f-list{list-style:none;font:400 13px/34px "Heebo",sans-serif;color:#333}
.f-contact{display:flex;align-items:center;gap:12px;font:400 13px/20px "Heebo",sans-serif;color:#333}
.ring{width:36px;height:36px;border-radius:50%;border:2px solid var(--green);display:flex;align-items:center;justify-content:center;flex:none}
.ring svg{width:16px;height:16px;stroke:#222;fill:none;stroke-width:1.8}
.rule{top:4832px;left:66px;width:1068px;height:1px;background:var(--line)}
.social{top:4850px;width:34px;height:34px;border-radius:50%;border:1px solid #999}
.social.first{background:var(--green);border-color:var(--green)}
.copy{font:400 13px "Heebo",sans-serif;color:#333}
.copy a{color:var(--green);text-decoration:none}
</style>
</head>
<body>

<!-- Header + hero -->
<section class="abs hero" role="img" aria-label="Dark photo of a janitor cleaning a commercial floor with a floor machine"></section>
<div class="abs hero-figure" role="img" aria-label="Large mascot illustration with glasses and moustache"></div>
<div class="abs logo" style="top:18px;left:66px"><span class="dot"></span>tilebaron</div>
<nav class="abs nav"><span class="on">Home</span><span>About Us</span><span>Services</span><span>Projects</span><span>Contact Us</span></nav>
<a class="abs btn quote">Get a quote</a>
<span class="abs tick" style="top:238px;left:66px"></span>
<h1 class="abs hero-title" style="top:252px;left:66px">Resurfacing and<br>power <em>washing</em></h1>
<p class="abs hero-text" style="top:378px;left:66px">Nor again is there anyone who loves or pursues or desires to obtain pain of itself</p>
<a class="abs btn" style="top:456px;left:66px;width:164px;height:46px">Get started</a>

<!-- Partners -->
<div class="abs center" style="top:740px"><span class="tick"></span></div>
<div class="abs center partners-title" style="top:766px">COMPANIES WE HAVE <em>WORK WITH</em></div>
<div class="abs partners">
  <span class="partner"><i></i>Lonestar Ohm</span>
  <span class="partner">Quillpoint</span>
  <span class="partner">keyway</span>
  <span class="partner">Routely</span>
  <span class="partner">nestora</span>
  <span class="partner"><i></i>Tallyset</span>
</div>

<!-- Welcome -->
<div class="abs welcome-frame"></div>
<div class="abs welcome-photo" role="img" aria-label="Worker kneeling while installing floor tiles in a warehouse"></div>
<div class="abs play"></div>
<span class="abs tick" style="top:994px;left:714px"></span>
<div class="abs label" style="top:1016px;left:714px">Welcome to</div>
<div class="abs title" style="top:1044px;left:714px">Tilebaron</div>
<p class="abs body-text" style="top:1128px;left:714px;width:420px">Nor again is there anyone who loves or pursues or desires to obtain pain of itself, because it is pain, but because occasionally circumstances occur in which toil and pain can procure him some great pleasure take a trivial example, which of us ever undertakes...</p>
<a class="abs btn" style="top:1292px;left:714px;width:156px;height:48px">Read more</a>

<!-- Services -->
<section class="abs services-band"></section>
<div class="abs center" style="top:1508px"><span class="tick" style="background:#fff"></span></div>
<div class="abs center label" style="top:1530px">What we do</div>
<div class="abs center title" style="top:1556px;color:#fff">Our services we offer</div>
<div class="abs center" style="top:1620px;font:400 15px Heebo,sans-serif;color:#e5e5e5">To take a trivial example, which of us ever undertakes laborious physical exercise, except to obtain some advantage from it</div>

<div class="abs svc-img" style="left:66px;background:linear-gradient(160deg,#3c6fa0,#2b4a6b 55%,#c24a3a)" role="img" aria-label="Carpet shampoo machine on a colourful carpet"></div>
<div class="abs svc-img" style="left:428px;background:linear-gradient(160deg,#5a7fa8,#3c4e63 50%,#e06a2a)" role="img" aria-label="Orange burnishing machine on a glossy floor"></div>
<div class="abs svc-img" style="left:790px;background:linear-gradient(160deg,#e4e6e8,#b9bec2 55%,#d7c23a)" role="img" aria-label="Yellow power washer in an industrial hall"></div>

<div class="abs svc-card" style="left:88px"><h3>Carpet Shampooing</h3><p>Quis autem vel eum iure reprehenderit qui in ea voluptate velit esse quam</p><a class="btn">Read more</a></div>
<div class="abs svc-card" style="left:450px"><h3>Burnishing</h3><p>Quis autem vel eum iure reprehenderit qui in ea voluptate velit esse quam</p><a class="btn">Read more</a></div>
<div class="abs svc-card" style="left:812px"><h3>Power Washing</h3><p>Quis autem vel eum iure reprehenderit qui in ea voluptate velit esse quam</p><a class="btn">Read more</a></div>

<!-- Projects -->
<div class="abs center" style="top:2262px"><span class="tick"></span></div>
<div class="abs center label" style="top:2284px">Projects</div>
<div class="abs center title" style="top:2310px">Different flooring</div>
<p class="abs center sub-dark" style="top:2382px;left:250px;right:250px">To take a trivial example, which of us ever undertakes laborious physical exercise, except to obtain some advantage from it</p>

<div class="abs tile" style="top:2467px;left:66px;width:349px;height:223px;background:linear-gradient(180deg,#3a3a3a,#c9b89a 55%,#d8c8a8)" role="img" aria-label="Meeting rooms with light wooden floor"></div>
<div class="abs tile" style="top:2702px;left:66px;width:349px;height:223px;background:linear-gradient(160deg,#3d7a2a,#2d5a1e)" role="img" aria-label="Office interior under a green overlay"></div>
<div class="abs tile-text" style="top:2778px;left:66px;width:349px"><b>TEMPORA INCIDUNT</b><span>Duis aute irure dolor in reprehenderit voluptate</span></div>
<div class="abs tile" style="top:2467px;left:426px;width:349px;height:458px;background:linear-gradient(180deg,#e8e6e0,#c9c4ba 50%,#5d5852)" role="img" aria-label="Office corridor with striped grey carpet and armchairs"></div>
<div class="abs tile" style="top:2467px;left:785px;width:349px;height:223px;background:linear-gradient(160deg,#6b7c8e,#3a3f52 50%,#3e5aa8)" role="img" aria-label="Hotel hallway with patterned blue and yellow carpet"></div>
<div class="abs tile" style="top:2702px;left:785px;width:349px;height:223px;background:linear-gradient(180deg,#dfe4e6,#b8c2c4 45%,#6f9a3a)" role="img" aria-label="Open office with green carpet and glass partitions"></div>

<!-- Testimonials -->
<section class="abs soft-bg"></section>
<div class="abs center" style="top:3072px"><span class="tick"></span></div>
<div class="abs center label" style="top:3094px">Testimonials</div>
<div class="abs center title" style="top:3120px">What our customer says</div>

<div class="abs quote-card" style="left:66px"></div>
<div class="abs avatar" style="left:66px;background:linear-gradient(160deg,#f3b43a,#e79a1f)" role="img" aria-label="Portrait of a smiling customer"></div>
<p class="abs quote-text" style="top:3246px;left:262px">“To take a trivial example, which of us ever undertakes laborious physical exercise, except to obtain some advantage But who has any right to find fault with a man”...</p>
<div class="abs who" style="top:3372px;left:262px"><b>ROWAN DELGADO</b><span>Designer</span></div>

<div class="abs quote-card" style="left:612px"></div>
<div class="abs avatar" style="left:612px;background:linear-gradient(160deg,#f3b43a,#e79a1f)" role="img" aria-label="Portrait of a smiling customer"></div>
<p class="abs quote-text" style="top:3246px;left:808px">“To take a trivial example, which of us ever undertakes laborious physical exercise, except to obtain some advantage But who has any right to find fault with a man”...</p>
<div class="abs who" style="top:3372px;left:808px"><b>ROWAN DELGADO</b><span>Designer</span></div>

<!-- Contact -->
<div class="abs center" style="top:3534px"><span class="tick"></span></div>
<div class="abs center label" style="top:3556px">Contact us</div>
<div class="abs center title" style="top:3582px">Get in touch with us</div>
<div class="abs contact-photo" role="img" aria-label="Cleaner operating a floor scrubber in a glass office lobby"></div>

<form class="abs form-card">
  <p class="intro">To take a trivial example, which of us ever undertakes laborious physical exercise except to obtain some advantage...</p>
  <div class="field active" style="top:108px">Jonah Pruitt |<svg viewBox="0 0 16 16"><circle cx="8" cy="5" r="3"/><path d="M2 15c1-4 11-4 12 0"/></svg></div>
  <div class="field" style="top:170px">Email address<svg viewBox="0 0 16 16"><rect x="1.5" y="3" width="13" height="10"/><path d="M1.5 3l6.5 5 6.5-5"/></svg></div>
  <div class="field" style="top:232px">Phone number<svg viewBox="0 0 16 16"><path d="M3 2l3 1 1 3-2 1c1 2 2 3 4 4l1-2 3 1 1 3c-6 1-12-5-11-11z"/></svg></div>
  <div class="field" style="top:294px">Services<svg viewBox="0 0 16 16"><path d="M4 6l4 4 4-4"/></svg></div>
  <div class="field msg" style="top:356px">Message<svg viewBox="0 0 16 16"><path d="M3 13l1-3 7-7 2 2-7 7z"/></svg></div>
  <a class="btn abs" style="left:188px;top:512px;width:156px;height:46px">Send now</a>
</form>

<!-- Footer -->
<div class="abs footer-logo" style="top:4578px;left:66px"><span class="dot"></span>tilebaron</div>
<p class="abs body-text" style="top:4652px;left:66px;width:330px;font-size:13px;line-height:22px;color:#333">Quis autem vel eum iure reprehenderit qui in ea voluptate velit esse quam nihil molestiae consequatur, vel illum qui dolorem eum fugiat quo voluptas nulla pariatur</p>

<div class="abs" style="top:4566px;left:488px"><div class="f-head">Quick links</div>
<ul class="f-list" style="margin-top:6px"><li>Home</li><li>About Us</li><li>Services</li><li>Projects</li><li>Contact Us</li></ul></div>

<div class="abs" style="top:4566px;left:672px"><div class="f-head">Services</div>
<ul class="f-list" style="margin-top:6px"><li>Carpet Shampooing</li><li>Burnishing</li><li>Resurfacing</li><li>Power washing</li></ul></div>

<div class="abs" style="top:4566px;left:888px"><div class="f-head">Contact us</div>
  <div class="f-contact" style="margin-top:14px"><span class="ring"><svg viewBox="0 0 16 16"><path d="M8 15s5-5 5-9A5 5 0 003 6c0 4 5 9 5 9z"/><circle cx="8" cy="6" r="1.6"/></svg></span>71 Quarry Bend Lane<br>Millbrook 90TQR USA</div>
  <div class="f-contact" style="margin-top:14px"><span class="ring"><svg viewBox="0 0 16 16"><path d="M3 2l3 1 1 3-2 1c1 2 2 3 4 4l1-2 3 1 1 3c-6 1-12-5-11-11z"/></svg></span>+2 (555) 240 6100</div>
  <div class="f-contact" style="margin-top:14px"><span class="ring"><svg viewBox="0 0 16 16"><rect x="1.5" y="3" width="13" height="10"/><path d="M1.5 3l6.5 5 6.5-5"/></svg></span><span style="color:#3b7bd4">info@tilebaron.org</span></div>
</div>

<div class="abs rule"></div>
<span class="abs social first" style="left:66px"></span>
<span class="abs social" style="left:112px"></span>
<span class="abs social" style="left:158px"></span>
<span class="abs social" style="left:204px"></span>
<div class="abs copy" style="top:4858px;right:66px">© <a>Tilebaron</a>, 2024. All Rights Reserved.</div>

</body>
</html>
```